Re-branding for Structural Engineering firm

We need new business cards as part of our current re-branding. We have a new logo (attached), so the card design should incorporate this color scheme. We are a structural engineering firm providing structural building design and seismic consulting services. The final design should communicate professionalism and stability, with a modern look and feel.

```html
<!DOCTYPE html>
<html lang="en">
<head>
<meta charset="utf-8">
<title>Kestrel Structural – Business Card</title>
<link rel="stylesheet" href="https://fonts.googleapis.com/css2?family=Lato:wght@400;700;900&display=swap">
<style>
  :root {
    --backdrop: #e9ebee;
    --card-black: #1b1b1c;
    --panel-white: #ffffff;
    --brand-blue: #1f72bf;
    --brand-grey: #8a8b8e;
    --ink: #111111;
  }
  * { box-sizing: border-box; margin: 0; padding: 0; }
  html, body {
    width: 1200px; height: 863px; overflow: hidden;
    background: var(--backdrop);
    font-family: "Lato", Arial, sans-serif;
  }
  .canvas { position: relative; width: 1200px; height: 863px; }
  .card {
    position: absolute; left: 420px; top: 116px;
    width: 360px; height: 630px;
    background: var(--card-black);
    box-shadow: 0 18px 40px rgba(0,0,0,0.18);
  }
  .card-shapes { position: absolute; inset: 0; }
  .brand {
    position: absolute; top: 120px; left: 0; width: 100%;
    display: flex; align-items: center; justify-content: center; gap: 12px;
  }
  .brand-square { width: 34px; height: 34px; background: var(--brand-blue); }
  .brand-name {
    color: #ffffff; font-weight: 700; font-size: 22px;
    letter-spacing: 0.06em; text-transform: uppercase;
  }
  .contact {
    position: absolute; top: 296px; left: 0; width: 100%;
    text-align: center; color: var(--ink);
  }
  .person-name { font-weight: 900; font-size: 24px; letter-spacing: 0.01em; }
  .person-title { font-weight: 700; font-size: 12px; letter-spacing: 0.04em; margin-top: 2px; }
  .details { font-weight: 700; font-size: 13.5px; line-height: 19px; }
  .details.phones { margin-top: 18px; }
  .details.office { margin-top: 12px; }
</style>
</head>
<body>
<main class="canvas">
  <article class="card">
    <svg class="card-shapes" width="360" height="630" viewBox="0 0 360 630" aria-hidden="true">
      <polygon class="info-panel" fill="var(--panel-white)"
        points="34,240 326,240 342,256 342,548 326,564 34,564 18,548 18,256"/>
      <rect class="accent-bar-blue" x="46" y="252" width="268" height="26" fill="var(--brand-blue)"/>
      <rect class="accent-bar-grey" x="46" y="520" width="268" height="30" fill="var(--brand-grey)"/>
    </svg>

    <div class="brand">
      <span class="brand-square"></span>
      <span class="brand-name">Kestrel Structural</span>
    </div>

    <div class="contact">
      <p class="person-name">REID CALLOWAY S.E.</p>
      <p class="person-title">PRINCIPAL</p>
      <p class="details phones">555.214.3081 &nbsp;|&nbsp; 555.738.4426<br>reid@kestrelse.com</p>
      <p class="details office">4170 Harbor Ridge Dr., Ste 210<br>Lakemont, CA 90417<br>555.214.3000 | www.kestrelse.com</p>
    </div>
  </article>
</main>
</body>
</html>
```